Flyer-Design für neues Produkt einer Druckerei
Zielgruppe
Wir sind eine Druckerei und seit vielen Jahren auf ökologische Werbemittel wie Parkscheiben, Drehscheiben usw. spezialisiert. Produktbeispiele finden Sie auf dem Slider bei www.lumora-satz.de.
In der Vergangenheit haben wir nur Kundenaufträge ausgeführt. Jetzt möchten wir aber eigene Produkte mit eigenen Designs an den Markt bringen. Wir sind aber ein produzierendes Unternehmen mit überschaubarem Know-how in Grafik & Design ==> wir suchen ständig Grafiker um von Fall zu Fall neue Designs für uns zu entwerfen.
Bei diesem Projekt geht es um die erste Seite eines neuen lumora-Produktes, einer Wasseruhr. Das Produkt sieht auf die die beiden Flyerparkscheiben auf Slide 13 bei www.lumora-satz.de. Mit einer Ausnahme.
Auf Seite 1 soll statt der Parkscheibenfunktion eine Wasseruhr kommen. Mit der Uhr kann man überwachen, wie viel man am Tag getrunken hat.
Die Überschrift (statt Ankunftszeit) lautet dann 'Wasseruhr' oder 'Haben Sie heute schon genügend getrunken' oder eine Idee von Ihnen.
Auf Seite eins findet sich außerdem ein Uhr in Kreisform mit den Zahlenwerten 0,1, 02, 03, 04, 0,5 .... bis 3,0 l.
Wir montieren auf Seite 1 einen Zeiger ==> man kann nach jedem Getränk einstellen wie viel man bis dahin am Tag getrunken hat.
Ziel des Wettbewerbs ist es nun ein schönes Design für Seite 1 zu finden. Wir haben zum Beispiel an einen Wassertropfen gedacht, in welchen man die 'Wasseruhr' einbauen kann. Das ist aber nur eine Idee.
SIE SIND VÖLLIG FREI IN IHREN VORSCHLÄGEN und wir sind wirklich gespannt auf Ihre Ideen.
Falls Sie mehr Informationen benötigen ==> einfach eine Mail an jonas.welkert@lumora-satz.de
Vielen Dank und vielleicht bis bald!
Jonas Welkert
Aufgabenstellung
Wir legen Wert auf eine effiziente Zusammenarbeit. Das bedeutet für uns
a) Eindeutige Definition der Aufgabenstellung
Diese Projektbeschreibung sollte alle wichtigen Punkte enthalten. In der Vergangenheit kam es gleichwohl immer wieder zu Missverständnissen ==> im Zweifel sollten Teilnehmer lieber ein mal mehr als weniger bei mir nachfragen
b) Die Teilnehmer am Wettbewerb erhalten von uns eine Druckstandskizze und eine Datei mit einem ähnlichen Produkt zur Anschauung
b) Vereinbarung von Deadlines
Diese sind immer lang genug und können bei Bedarf auch verschoben werden. Gleichwohl halten wir Deadlines für
eine hilfreiches Tool auch bei Kreativprojekten.
c) Eine eindeutige Definition in welchem Dateiformat die Arbeitsergebnisse geliefert werden sollen
Wir bitten um Verständnis für den Punkt. Aber in der Vergangenheit gab es hier des öfteren Male Missverstädnisse
d) Die Vorschläge/Designs für den Wettbewerb bitte als pdf in das Projekt einstellen
e) Vom Sieger des Wettbewerbs erhalten wir die Daten dann bitte als offene Indesigndatei

```html
<!DOCTYPE html>
<html lang="de">
<head>
<meta charset="utf-8">
<title>Wasseruhr – Flyer Seite 1</title>
<link rel="stylesheet" href="https://fonts.googleapis.com/css2?family=Open+Sans:ital,wght@0,700;0,800;1,600&display=swap">
<style>
  :root {
    --page-bg: #8e8f93;
    --leaf-dark: #4f7d24;
    --leaf-light: #9cc254;
    --wood-dark: #5e3f2a;
    --wood-light: #8c6244;
    --badge-green: #2f6b3c;
    --badge-green-light: #5a9a64;
    --ink-white: #ffffff;
    --needle: #ecefec;
    --pivot: #3a3a3a;
  }
  html, body {
    margin: 0;
    width: 1200px;
    height: 1200px;
    overflow: hidden;
    background: var(--page-bg);
  }
  .flyer {
    position: absolute;
    left: 204px;
    top: 60px;
    width: 792px;
    height: 1080px;
    overflow: hidden;
  }
  .flyer__photo {
    position: absolute;
    inset: 0;
    background: linear-gradient(180deg,
      var(--leaf-dark) 0%,
      #6f9a35 25%,
      var(--leaf-light) 45%,
      #7fa848 62%,
      var(--wood-dark) 74%,
      var(--wood-light) 88%,
      #9a6d4c 100%);
  }
  .flyer__title {
    position: absolute;
    top: 36px;
    left: 0;
    width: 100%;
    margin: 0;
    text-align: center;
    font-family: "Open Sans", sans-serif;
    font-weight: 800;
    font-size: 82px;
    letter-spacing: 6px;
    color: var(--ink-white);
  }
  .flyer__dial {
    position: absolute;
    inset: 0;
  }
  .dial__label {
    font-family: "Open Sans", sans-serif;
    font-weight: 700;
    fill: var(--ink-white);
    text-anchor: middle;
    dominant-baseline: central;
  }
  .flyer__tagline {
    position: absolute;
    top: 1016px;
    left: 0;
    width: 100%;
    margin: 0;
    text-align: center;
    font-family: "Open Sans", sans-serif;
    font-style: italic;
    font-weight: 600;
    font-size: 34px;
    letter-spacing: 1px;
    color: var(--ink-white);
  }
</style>
</head>
<body>
<main class="flyer">
  <div class="flyer__photo" role="img" aria-label="Foto: Wasser wird in ein Glas gegossen, Glas steht auf einem Holztisch vor grünem, unscharfem Hintergrund"></div>

  <h1 class="flyer__title">WASSERUHR</h1>

  <svg class="flyer__dial" viewBox="0 0 792 1080" width="792" height="1080" aria-label="Wasseruhr-Skala von 0 bis 3 Liter">
    <defs>
      <radialGradient id="badgeFill" cx="40%" cy="35%" r="70%">
        <stop offset="0%" stop-color="var(--badge-green-light)"/>
        <stop offset="100%" stop-color="var(--badge-green)"/>
      </radialGradient>
    </defs>

    <g class="dial__ticks" stroke="var(--ink-white)" stroke-linecap="butt">
      <line x1="391" y1="229" x2="391" y2="322" stroke-width="9" transform="rotate(0 391 544)"/>
      <line x1="391" y1="229" x2="391" y2="322" stroke-width="3" transform="rotate(12 391 544)"/>
      <line x1="391" y1="229" x2="391" y2="322" stroke-width="3" transform="rotate(24 391 544)"/>
      <line x1="391" y1="229" x2="391" y2="322" stroke-width="3" transform="rotate(36 391 544)"/>
      <line x1="391" y1="229" x2="391" y2="322" stroke-width="3" transform="rotate(48 391 544)"/>
      <line x1="391" y1="229" x2="391" y2="322" stroke-width="9" transform="rotate(60 391 544)"/>
      <line x1="391" y1="229" x2="391" y2="322" stroke-width="3" transform="rotate(72 391 544)"/>
      <line x1="391" y1="229" x2="391" y2="322" stroke-width="3" transform="rotate(84 391 544)"/>
      <line x1="391" y1="229" x2="391" y2="322" stroke-width="3" transform="rotate(96 391 544)"/>
      <line x1="391" y1="229" x2="391" y2="322" stroke-width="3" transform="rotate(108 391 544)"/>
      <line x1="391" y1="229" x2="391" y2="322" stroke-width="9" transform="rotate(120 391 544)"/>
      <line x1="391" y1="229" x2="391" y2="322" stroke-width="3" transform="rotate(132 391 544)"/>
      <line x1="391" y1="229" x2="391" y2="322" stroke-width="3" transform="rotate(144 391 544)"/>
      <line x1="391" y1="229" x2="391" y2="322" stroke-width="3" transform="rotate(156 391 544)"/>
      <line x1="391" y1="229" x2="391" y2="322" stroke-width="3" transform="rotate(168 391 544)"/>
      <line x1="391" y1="229" x2="391" y2="322" stroke-width="9" transform="rotate(180 391 544)"/>
      <line x1="391" y1="229" x2="391" y2="322" stroke-width="3" transform="rotate(192 391 544)"/>
      <line x1="391" y1="229" x2="391" y2="322" stroke-width="3" transform="rotate(204 391 544)"/>
      <line x1="391" y1="229" x2="391" y2="322" stroke-width="3" transform="rotate(216 391 544)"/>
      <line x1="391" y1="229" x2="391" y2="322" stroke-width="3" transform="rotate(228 391 544)"/>
      <line x1="391" y1="229" x2="391" y2="322" stroke-width="9" transform="rotate(240 391 544)"/>
      <line x1="391" y1="229" x2="391" y2="322" stroke-width="3" transform="rotate(252 391 544)"/>
      <line x1="391" y1="229" x2="391" y2="322" stroke-width="3" transform="rotate(264 391 544)"/>
      <line x1="391" y1="229" x2="391" y2="322" stroke-width="3" transform="rotate(276 391 544)"/>
      <line x1="391" y1="229" x2="391" y2="322" stroke-width="3" transform="rotate(288 391 544)"/>
      <line x1="391" y1="229" x2="391" y2="322" stroke-width="9" transform="rotate(300 391 544)"/>
      <line x1="391" y1="229" x2="391" y2="322" stroke-width="3" transform="rotate(312 391 544)"/>
      <line x1="391" y1="229" x2="391" y2="322" stroke-width="3" transform="rotate(324 391 544)"/>
      <line x1="391" y1="229" x2="391" y2="322" stroke-width="3" transform="rotate(336 391 544)"/>
      <line x1="391" y1="229" x2="391" y2="322" stroke-width="3" transform="rotate(348 391 544)"/>
    </g>

    <g class="dial__badges">
      <g class="badge">
        <circle cx="391" cy="176" r="52" fill="url(#badgeFill)"/>
        <circle cx="366" cy="150" r="6" fill="var(--ink-white)"/>
        <text class="dial__label" x="391" y="180" font-size="30">3L</text>
      </g>
      <g class="badge">
        <circle cx="710" cy="360" r="46" fill="url(#badgeFill)"/>
        <circle cx="688" cy="337" r="6" fill="var(--ink-white)"/>
        <text class="dial__label" x="710" y="364" font-size="22">0,5L</text>
      </g>
      <g class="badge">
        <circle cx="710" cy="728" r="52" fill="url(#badgeFill)"/>
        <circle cx="685" cy="702" r="6" fill="var(--ink-white)"/>
        <text class="dial__label" x="710" y="732" font-size="30">1L</text>
      </g>
      <g class="badge">
        <circle cx="391" cy="912" r="46" fill="url(#badgeFill)"/>
        <circle cx="369" cy="889" r="6" fill="var(--ink-white)"/>
        <text class="dial__label" x="391" y="916" font-size="22">1,5L</text>
      </g>
      <g class="badge">
        <circle cx="72" cy="728" r="52" fill="url(#badgeFill)"/>
        <circle cx="47" cy="702" r="6" fill="var(--ink-white)"/>
        <text class="dial__label" x="72" y="732" font-size="30">2L</text>
      </g>
      <g class="badge">
        <circle cx="72" cy="360" r="46" fill="url(#badgeFill)"/>
        <circle cx="50" cy="337" r="6" fill="var(--ink-white)"/>
        <text class="dial__label" x="72" y="364" font-size="22">2,5L</text>
      </g>
    </g>

    <g class="dial__needle" transform="rotate(36 391 544)">
      <path d="M391 236 L403 470 Q420 540 391 566 Q362 540 379 470 Z" fill="var(--needle)"/>
      <circle cx="391" cy="544" r="22" fill="var(--needle)"/>
    </g>
    <circle class="dial__pivot" cx="391" cy="544" r="6" fill="var(--pivot)"/>
  </svg>

  <p class="flyer__tagline">Stille Wasser sind gesund!</p>
</main>
</body>
</html>
```